Coralview Health Academy Open House

We need to create an advertisement for an upcoming open house that we are conducting. We can create a design in the dimensions of 10" (w) x 13.67" (h). Once that is approved, I will need the ad resized in the following dimensions:

8.5" (w) x 11" (h) - PDF
2400 pixels wide X 2400 pixels height - JPEG

Target Market(s)

Aspiring medical students

Industry/Entity Type

Medical

Requirements
Must have
• Logo
• Tag line: STUDY MEDICINE IN THE CARIBBEAN, BECOME A DOC IN THE US
• One of the attachments has a JPEG file with all the information to include in this new ad however the event location has changed to this:
• Sunday, April 22nd at 1pm at:
• Lantern Lodge Chicago Depot Square
• 718 N. Birch Court
• Chicago, IL 60654
• Event will be held on the 15th floor in The Penwick Room
• FREE parking. Refreshments will be served.
• Change email to admissions@chaheal.org
• Use a nice background and creative design. The details of the event need to be big and emphasize OPEN HOUSE.

```html
<!DOCTYPE html>
<html lang="en">
<head>
<meta charset="utf-8">
<title>Coralview Health Academy Open House</title>
<link rel="stylesheet" href="https://fonts.googleapis.com/css2?family=Roboto+Condensed:ital,wght@0,400;0,700;0,900;1,700&display=swap">
<style>
  :root {
    --navy: #24508e;
    --navy-deep: #1c2451;
    --blue-panel: #3c5f9c;
    --blue-panel-dark: #2f4c86;
    --red: #9b2129;
    --red-bright: #a8262e;
    --white: #ffffff;
    --page: #eceef1;
    --ink: #2a2a2a;
  }
  * { margin: 0; padding: 0; box-sizing: border-box; }
  html, body { width: 680px; height: 1200px; overflow: hidden; }
  body {
    background: var(--page);
    font-family: "Roboto Condensed", "Arial Narrow", sans-serif;
    position: relative;
  }
  .flyer {
    position: absolute; left: 20px; top: 162px;
    width: 640px; height: 876px;
    background: var(--white);
    overflow: hidden;
  }
  .headline {
    position: absolute; top: 28px; left: 0; width: 100%;
    text-align: center;
    font-weight: 900; font-size: 86px; line-height: 1; letter-spacing: 1px;
    text-shadow: 3px 3px 0 #3a3a3a;
  }
  .headline .open { color: var(--navy); }
  .headline .house { color: var(--red); }
  .stripe-red { position: absolute; left: 0; width: 100%; background: var(--red-bright); }
  .stripe-top { top: 132px; height: 11px; }
  .tagline-band {
    position: absolute; top: 143px; left: 0; width: 100%; height: 89px;
    background: var(--navy);
  }
  .stripe-bottom { top: 232px; height: 13px; }
  .tagline {
    position: absolute; top: 150px; left: 262px; width: 340px;
    text-align: center; color: var(--white); font-weight: 700; line-height: 1.05;
  }
  .tagline .t1 { font-size: 36px; }
  .tagline .t2 { font-size: 22px; }
  .tagline .t3 { font-size: 18px; margin-top: 3px; }
  .logo {
    position: absolute; left: 57px; top: 120px;
    width: 184px; height: 184px; border-radius: 50%;
    background: var(--white);
    border: 3px solid #c9ccd3;
    display: flex; align-items: center; justify-content: center;
    text-align: center; z-index: 3;
  }
  .logo span {
    color: var(--navy); font-weight: 700; font-size: 22px; line-height: 1.15;
    width: 130px;
  }
  .photo {
    position: absolute; top: 245px; left: 0; width: 100%; height: 370px;
    background:
      radial-gradient(ellipse at 30% 25%, #8fae5f 0%, transparent 55%),
      radial-gradient(ellipse at 75% 20%, #6f8f44 0%, transparent 50%),
      linear-gradient(180deg, #7e9a55 0%, #4d5f3a 50%, #1f2640 100%);
  }
  .date-box {
    position: absolute; left: 348px; top: 540px; width: 264px; height: 75px;
    background: var(--red); color: var(--white);
    text-align: center; font-weight: 700; padding-top: 10px; line-height: 1.2;
  }
  .date-box .day { font-size: 25px; }
  .date-box .when { font-size: 21px; }
  .date-box sup { font-size: 11px; }
  .venue {
    position: absolute; left: 348px; top: 615px; width: 264px; height: 161px;
    background: var(--blue-panel); color: var(--white); text-align: center;
  }
  .venue .address {
    font-size: 16px; line-height: 1.32; padding-top: 8px; padding-bottom: 8px;
    border-bottom: 1px solid rgba(255,255,255,.35); margin: 0 12px;
  }
  .venue .floor { font-size: 14px; margin-top: 8px; }
  .venue .floor sup { font-size: 8px; }
  .venue .room { font-size: 24px; line-height: 1.1; }
  .perks {
    position: absolute; left: 348px; top: 776px; width: 264px; height: 100px;
    background: var(--blue-panel-dark); color: var(--white); text-align: center;
    font-style: italic; font-weight: 700; padding-top: 16px;
  }
  .perks .p1 { font-size: 19px; }
  .perks .p2 { font-size: 14px; }
  .features {
    position: absolute; left: 28px; top: 628px; list-style: none;
  }
  .features li {
    display: flex; align-items: center; gap: 10px;
    font-style: italic; font-weight: 700; font-size: 21px; color: var(--navy-deep);
    height: 25.5px;
  }
  .features svg { width: 22px; height: 20px; flex: none; }
  .brace { position: absolute; left: 240px; top: 648px; }
  .extras {
    position: absolute; left: 252px; top: 650px; width: 96px;
    font-size: 12px; line-height: 1.25; color: var(--ink);
  }
  .extras p { margin-bottom: 9px; }
  .contact {
    position: absolute; left: 0; top: 775px; width: 348px; height: 77px;
    background: var(--red); color: var(--white); text-align: center;
    font-size: 13.5px; line-height: 1.3; padding-top: 6px;
  }
  .contact strong { font-style: italic; font-size: 15px; }
  .edge-red {
    position: absolute; left: 612px; top: 776px; width: 28px; height: 77px;
    background: var(--red);
  }
</style>
</head>
<body>
  <main class="flyer">
    <h1 class="headline"><span class="open">OPEN</span> <span class="house">HOUSE</span></h1>

    <div class="stripe-red stripe-top"></div>
    <div class="tagline-band"></div>
    <div class="stripe-red stripe-bottom"></div>

    <div class="logo"><span>Coralview Health Academy</span></div>

    <div class="tagline">
      <div class="t1">STUDY MEDICINE</div>
      <div class="t2">IN THE CARIBBEAN,</div>
      <div class="t3">BECOME A DOC IN THE US</div>
    </div>

    <div class="photo" role="img" aria-label="Photo of smiling graduates in caps and gowns raising diplomas outdoors under trees"></div>

    <div class="date-box">
      <div class="day">SUNDAY,</div>
      <div class="when">APRIL 22<sup>ND</sup> AT 1PM AT</div>
    </div>

    <section class="venue">
      <div class="address">
        LANTERN LODGE CHICAGO<br>DEPOT SQUARE<br>718 N. BIRCH COURT<br>CHICAGO, IL 60654
      </div>
      <div class="floor">Event will be held on the 15<sup>th</sup> floor</div>
      <div class="room">in The Penwick Room</div>
    </section>

    <ul class="features">
      <li><svg viewBox="0 0 22 20"><path d="M2 11 L8 17 L20 2" fill="none" stroke="#9b2129" stroke-width="4"/></svg>4 Year MD Program</li>
      <li><svg viewBox="0 0 22 20"><path d="M2 11 L8 17 L20 2" fill="none" stroke="#9b2129" stroke-width="4"/></svg>Financial Aid</li>
      <li><svg viewBox="0 0 22 20"><path d="M2 11 L8 17 L20 2" fill="none" stroke="#9b2129" stroke-width="4"/></svg>Student Dorms</li>
      <li><svg viewBox="0 0 22 20"><path d="M2 11 L8 17 L20 2" fill="none" stroke="#9b2129" stroke-width="4"/></svg>Moder Campus</li>
      <li><svg viewBox="0 0 22 20"><path d="M2 11 L8 17 L20 2" fill="none" stroke="#9b2129" stroke-width="4"/></svg>Friendly Tuition</li>
    </ul>

    <svg class="brace" width="12" height="104" viewBox="0 0 12 104">
      <path d="M11 1 Q5 1 5 8 L5 44 Q5 52 1 52 Q5 52 5 60 L5 96 Q5 103 11 103" fill="none" stroke="#2a2a2a" stroke-width="1.4"/>
    </svg>
    <div class="extras">
      <p>U.S. Clinical<br>Rotations</p>
      <p>88.9% USMLE<br>Passing Rate</p>
      <p>Canadian Loans<br>Available</p>
    </div>

    <section class="contact">
      For More details, email : admissions@chaheal.org<br>
      or <strong>Call : 888-555-0142</strong><br>
      Have Your entire application fee waived.<br>
      Enter Copon Code: OPHUS
    </section>
    <div class="edge-red"></div>

    <section class="perks">
      <div class="p1">FREE parking.</div>
      <div class="p2">Refreshments will be served.</div>
    </section>
  </main>
</body>
</html>
```